Ridgemule wrap for Women's Fitness Studio - KORVANTE

Create a Ridgemule wrap design for Women's Fitness Studio - KORVANTE.
This wrap print will need to accommodate for wrapping the edges, so you will need to get the proper measurements to make sure your design is a proper fit.
==============
TEXT:
Business Name: KORVANTE
Tag line: Fitness for Women
Keywords: Personal Training, Group Classes, Build Lean Muscle,
Lose Body Fat, Gain Strength & Confidence,
Website: korvante.com
QR Code and Keyword: Free Trial.
=============
Our Logo is attached.
Check our website and Instagram to get a better idea of our business.
www.korvante.com
IG: korvante.fitness
Design Elements (Black Wrap, White Lettering), other colors (Gray/Dark Gray/Silver). It would be interesting to see samples with solid colors and color fade, and design elements variations. We are also open to designs with other colors... Just bring your best ideas and we will consider them.
It's a fast car... so anything that resembles speed is of interest, but the main message should be fitness-oriented.
Ask questions if my description is not clear.
Other font styles liked:
- get ideas for Fonts from our Website (www.korvante.com)
Colors
Designer to choose colors to be used in the design.

```html
<!DOCTYPE html>
<html lang="en">
<head>
<meta charset="utf-8">
<title>KORVANTE – Ridgemule Wrap Layout</title>
<link rel="stylesheet" href="https://fonts.googleapis.com/css2?family=Bitter:ital,wght@1,500&family=Montserrat:wght@600;700;800&display=swap">
<style>
  :root {
    --canvas: #474747;
    --body: #1a1a1c;
    --roof: #141415;
    --brand-red: #d3174c;
    --brand-red-deep: #5a0a1e;
    --rear-red: #e3141c;
    --white: #ffffff;
    --silver-light: #f2f2f2;
    --silver-dark: #8a8a8a;
  }
  html, body {
    margin: 0;
    width: 1200px;
    height: 2186px;
    overflow: hidden;
    background: var(--canvas);
  }
  .wrap-sheet { display: block; width: 1200px; height: 2186px; }
  .body-panel { fill: var(--body); }
  .roof-line { fill: none; stroke: var(--roof); stroke-width: 10; stroke-linejoin: round; }
  .silver-edge { fill: none; stroke: url(#silver); stroke-width: 7; }
  .speed-stripe { stroke: var(--brand-red); stroke-width: 2.2; }
  .brand-name {
    font-family: "Montserrat", sans-serif;
    font-weight: 600;
    fill: var(--white);
    letter-spacing: 3px;
  }
  .brand-mark { fill: var(--white); }
  .tagline {
    font-family: "Bitter", serif;
    font-style: italic;
    font-weight: 500;
    font-size: 15px;
    fill: var(--white);
  }
  .tagline .accent { fill: var(--brand-red); }
  .phone {
    font-family: "Montserrat", sans-serif;
    font-weight: 800;
    font-size: 20px;
    fill: var(--white);
  }
  .web {
    font-family: "Montserrat", sans-serif;
    font-weight: 700;
    font-size: 12px;
    fill: var(--white);
  }
  .rear-headline {
    font-family: "Montserrat", sans-serif;
    font-weight: 800;
    font-size: 14px;
    fill: var(--rear-red);
  }
  .rear-trim { fill: none; stroke: var(--rear-red); stroke-width: 14; }
  .rear-block { fill: var(--rear-red); }
  .plate { fill: #0e0e0e; }
</style>
</head>
<body>
<svg class="wrap-sheet" viewBox="0 0 1200 2186" xmlns="http://www.w3.org/2000/svg">
  <defs>
    <linearGradient id="silver" x1="0" y1="0" x2="1" y2="1">
      <stop offset="0" stop-color="var(--silver-dark)"/>
      <stop offset="0.5" stop-color="var(--silver-light)"/>
      <stop offset="1" stop-color="var(--silver-dark)"/>
    </linearGradient>
    <linearGradient id="photo-tone" x1="0" y1="0" x2="0" y2="1">
      <stop offset="0" stop-color="#c51446"/>
      <stop offset="0.55" stop-color="#9b0f35"/>
      <stop offset="1" stop-color="#3a0714"/>
    </linearGradient>
    <linearGradient id="band-fade" x1="0" y1="0" x2="1" y2="0">
      <stop offset="0" stop-color="var(--brand-red)"/>
      <stop offset="1" stop-color="#b0123f"/>
    </linearGradient>
    <pattern id="hood-stripes" width="7" height="10" patternUnits="userSpaceOnUse">
      <rect width="7" height="10" fill="#120507"/>
      <rect width="3" height="10" fill="var(--brand-red)"/>
    </pattern>
    <linearGradient id="hood-fade" x1="0" y1="0" x2="0" y2="1">
      <stop offset="0" stop-color="#0c0c0d" stop-opacity="0"/>
      <stop offset="0.55" stop-color="#0c0c0d" stop-opacity="0.85"/>
      <stop offset="1" stop-color="#0c0c0d" stop-opacity="1"/>
    </linearGradient>
    <clipPath id="side-clip">
      <polygon points="170,140 720,80 732,28 1060,80 1060,170 1000,175 950,92 850,92 795,222 410,226 350,95 250,95 195,186 170,186"/>
    </clipPath>
  </defs>

  <!-- Passenger side panel -->
  <g class="side-panel side-right" transform="translate(0,250)">
    <polyline class="roof-line" points="170,132 550,5 700,16 1060,72"/>
    <polygon class="body-panel" points="170,140 720,80 732,28 1060,80 1060,170 1000,175 950,92 850,92 795,222 410,226 350,95 250,95 195,186 170,186"/>
    <g clip-path="url(#side-clip)">
      <polygon fill="url(#band-fade)" points="855,60 1060,72 1060,98 850,112"/>
      <polygon fill="url(#photo-tone)" points="705,20 860,20 790,230 655,230" role="img" aria-label="Photo of a trainer in white sportswear in a lunge pose with a measuring tape"/>
      <polygon fill="var(--brand-red)" points="560,230 655,230 668,190"/>
      <g class="speed-stripes">
        <line class="speed-stripe" x1="420" y1="192" x2="655" y2="186"/>
        <line class="speed-stripe" x1="420" y1="197" x2="652" y2="191"/>
        <line class="speed-stripe" x1="420" y1="202" x2="650" y2="196"/>
        <line class="speed-stripe" x1="420" y1="207" x2="648" y2="201"/>
        <line class="speed-stripe" x1="420" y1="212" x2="646" y2="206"/>
        <line class="speed-stripe" x1="420" y1="217" x2="644" y2="211"/>
        <line class="speed-stripe" x1="420" y1="222" x2="642" y2="216"/>
      </g>
      <path class="silver-edge" d="M708,20 Q690,130 656,232"/>
      <path class="silver-edge" d="M862,40 Q818,140 792,232"/>
    </g>
    <rect class="brand-mark" x="503" y="118" width="24" height="24"/>
    <text class="brand-name" x="515" y="176" font-size="22" text-anchor="middle">KORVANTE</text>
    <text class="tagline" text-anchor="end">
      <tspan x="672" y="128">Personal Fitness</tspan>
      <tspan x="660" y="143">Training for</tspan>
      <tspan class="accent" x="640" y="157">Women</tspan>
    </text>
    <text class="phone" x="865" y="104" transform="rotate(-2 865 104)">415-555-0148</text>
    <text class="web" x="865" y="124" transform="rotate(-2 865 124)">www.korvante.com</text>
  </g>

  <!-- Driver side panel (mirrored) -->
  <g class="side-panel side-left" transform="translate(0,790)">
    <g transform="translate(1200,0) scale(-1,1)">
      <polyline class="roof-line" points="170,132 550,5 700,16 1060,72"/>
      <polygon class="body-panel" points="170,140 720,80 732,28 1060,80 1060,170 1000,175 950,92 850,92 795,222 410,226 350,95 250,95 195,186 170,186"/>
      <g clip-path="url(#side-clip)">
        <polygon fill="url(#band-fade)" points="855,60 1060,72 1060,98 850,112"/>
        <polygon fill="url(#photo-tone)" points="705,20 860,20 790,230 655,230" role="img" aria-label="Photo of a trainer in magenta sportswear holding a foam roller and a water bottle with a measuring tape"/>
        <polygon fill="var(--brand-red)" points="560,230 655,230 668,190"/>
        <line class="speed-stripe" x1="420" y1="192" x2="655" y2="186"/>
        <line class="speed-stripe" x1="420" y1="197" x2="652" y2="191"/>
        <line class="speed-stripe" x1="420" y1="202" x2="650" y2="196"/>
        <line class="speed-stripe" x1="420" y1="207" x2="648" y2="201"/>
        <line class="speed-stripe" x1="420" y1="212" x2="646" y2="206"/>
        <line class="speed-stripe" x1="420" y1="217" x2="644" y2="211"/>
        <line class="speed-stripe" x1="420" y1="222" x2="642" y2="216"/>
        <path class="silver-edge" d="M708,20 Q690,130 656,232"/>
        <path class="silver-edge" d="M862,40 Q818,140 792,232"/>
      </g>
    </g>
    <rect class="brand-mark" x="673" y="118" width="24" height="24"/>
    <text class="brand-name" x="685" y="176" font-size="22" text-anchor="middle">KORVANTE</text>
    <text class="tagline">
      <tspan x="526" y="128">Personal Fitness</tspan>
      <tspan x="538" y="143">Training for</tspan>
      <tspan class="accent" x="556" y="157">Women</tspan>
    </text>
    <text class="phone" x="195" y="100" transform="rotate(2 195 100)">415-555-0148</text>
    <text class="web" x="195" y="120" transform="rotate(2 195 120)">www.korvante.com</text>
  </g>

  <!-- Front hood panel -->
  <g class="front-panel" transform="translate(70,1500) scale(0.92)">
    <polygon fill="url(#hood-stripes)" points="70,0 550,0 605,90 580,190 310,210 25,190 0,90"/>
    <polygon fill="url(#hood-fade)" points="70,0 550,0 605,90 580,190 310,210 25,190 0,90"/>
    <rect class="brand-mark" x="288" y="22" width="28" height="28"/>
    <text class="brand-name" x="302" y="96" font-size="30" letter-spacing="5" text-anchor="middle">KORVANTE</text>
  </g>

  <!-- Rear tailgate panel -->
  <g class="rear-panel" transform="translate(660,1440)">
    <polyline class="rear-trim" points="100,0 30,170 30,260"/>
    <polyline class="rear-trim" points="410,0 480,170 480,260"/>
    <line x1="88" y1="30" x2="96" y2="10" stroke="var(--white)" stroke-width="14"/>
    <line x1="422" y1="30" x2="414" y2="10" stroke="var(--white)" stroke-width="14"/>
    <rect class="rear-block" x="24" y="164" width="110" height="14"/>
    <rect class="rear-block" x="376" y="164" width="110" height="14"/>
    <rect class="rear-block" x="0" y="240" width="70" height="75"/>
    <rect class="rear-block" x="440" y="240" width="70" height="75"/>
    <rect class="plate" x="30" y="205" width="450" height="75"/>
    <rect class="plate" x="70" y="270" width="370" height="45"/>
    <rect class="brand-mark" x="140" y="225" width="20" height="20"/>
    <text class="brand-name" x="150" y="292" font-size="16" letter-spacing="2" text-anchor="middle">KORVANTE</text>
    <text class="rear-headline" text-anchor="middle">
      <tspan x="365" y="232">PERSONAL FITNESS</tspan>
      <tspan x="365" y="246">TRAINING FOR</tspan>
      <tspan x="365" y="260">WOMEN</tspan>
    </text>
    <text class="phone" x="368" y="286" font-size="14" text-anchor="middle">415-555-0148</text>
    <text class="web" x="368" y="302" font-size="10" text-anchor="middle">www.korvante.com</text>
  </g>
</svg>
</body>
</html>
```